Internationally renowned Business Coach and Public Speaker needs new Website

I need a website to further support and expand my personal brand - I am a well known entrepreneur, business coach and public speaker on the thema of 'Business Acceleration' and I regularly write articles and have written a popular managementbook on this thema. I would like a new, visually strong and exciting website to explain my background and added value as a business coach and keynote speaker. As a reference I would like to point out the website of Tem Vasko (www.temvasko.com).

Target Market(s)

top CEO's of international companies

Industry/Entity Type

Business

Number of Pages Required

1 page

Requirements
Nice to have
• us as a reference: www.temvasko.com

```html
<!DOCTYPE html>
<html lang="en">
<head>
<meta charset="utf-8">
<title>Apexa Growth Partners</title>
<link rel="stylesheet" href="https://fonts.googleapis.com/css2?family=Noto+Sans:wght@400;700&family=Open+Sans:wght@400;600;700&display=swap">
<style>
:root{
  --red:#d0111b;
  --red-dark:#a80a12;
  --ink:#3a3a3a;
  --text:#777;
  --paper:#f3f2ef;
  --paper-light:#f8f8f7;
  --charcoal:#242424;
  --grey-band:#e4e4e4;
  --white:#fff;
}
*{box-sizing:border-box;margin:0;padding:0}
html,body{width:1200px;height:2270px;overflow:hidden}
body{position:relative;background:var(--paper);font-family:"Open Sans",Arial,sans-serif;color:var(--text)}
.abs{position:absolute}
h1,h2,h3,.pill{font-family:"Noto Sans",Arial,sans-serif}

/* header */
.site-header{left:0;top:0;width:1200px;height:120px;background:var(--paper-light);border-top:3px solid var(--red)}
.brand{display:flex;align-items:center;gap:12px}
.brand-mark{width:62px;height:62px;border-radius:50%;background:var(--red)}
.brand-name{font-family:"Noto Sans",Arial,sans-serif;font-weight:700;font-size:16px;line-height:17px;color:#555;width:110px}
.site-header .brand{left:110px;top:28px}
.social{display:flex;gap:10px}
.social span{width:36px;height:36px;border-radius:50%;background:var(--red);display:block}
.site-header .social{left:638px;top:12px}
.call-tab{left:822px;top:0;width:266px;height:48px;background:var(--red);border-radius:0 0 26px 26px;color:var(--white);font-size:15px;display:flex;align-items:center;justify-content:center;gap:10px}
.main-nav{left:458px;top:82px;display:flex;font-size:12px;font-weight:600;color:#333}
.main-nav a{color:inherit;text-decoration:none;margin-right:38px}
.main-nav a.active{color:var(--red)}

/* hero */
.hero{left:0;top:120px;width:1200px;height:468px;border-bottom:3px solid var(--red);background:linear-gradient(100deg,#7a6f6a 0%,#b9aaa2 35%,#8c7f78 60%,#3c3a3e 100%)}
.hero-title{left:110px;top:305px;font-size:40px;font-weight:400;color:var(--white);letter-spacing:.5px}
.hero-rule{left:110px;top:368px;width:605px;height:1px;background:rgba(255,255,255,.55)}
.hero-lead{left:113px;top:386px;width:610px;font-size:11.5px;line-height:26px;color:var(--white);font-weight:600}
.dots{left:561px;top:551px;display:flex;gap:8px}
.dots i{width:12px;height:12px;border-radius:50%;background:#bbb;border:1px solid #999;display:block}
.dots i.on{background:var(--red)}

/* service cards */
.services{left:0;top:590px;width:1200px;height:285px;background:var(--paper)}
.card{top:625px;width:309px;height:182px;border-radius:8px;overflow:hidden}
.card.coach{left:110px;background:linear-gradient(135deg,#8e3fa3,#d98ad8 60%,#6a2a7a)}
.card.speaker{left:445px;background:linear-gradient(135deg,#3a2a25,#7a4a30 60%,#2a2220)}
.card.programs{left:779px;background:linear-gradient(135deg,#4a4f8a,#b09a8c 50%,#2f3460)}
.card-note{left:469px;top:633px;width:262px;height:128px;background:rgba(20,20,20,.85);border-radius:18px;color:var(--white);font-size:11px;line-height:24px;text-align:justify;padding:10px 20px;overflow:hidden}
.pill{top:769px;width:262px;height:72px;border-radius:30px;background:linear-gradient(#5a5a5a,#3d3d3d);color:var(--white);font-size:21px;display:flex;align-items:center;justify-content:center;box-shadow:0 4px 6px rgba(0,0,0,.25)}
.pill.red{background:linear-gradient(#e0141f,#b30b13)}

/* expertise */
.expertise{left:0;top:875px;width:1200px;height:317px;background:var(--paper-light);border-top:1px solid #ddd;border-bottom:1px solid #ddd}
.section-title{width:1200px;left:0;text-align:center;color:var(--ink);font-weight:400}
.expertise .section-title{top:45px;font-size:32px}
.expertise-copy{left:112px;top:98px;width:976px;font-size:11.5px;line-height:29px;text-align:justify;color:#888}
.events-btn{left:481px;top:202px;width:238px;height:61px;border-radius:30px;background:linear-gradient(#555,#3a3a3a);color:var(--white);font-size:15px;font-weight:700;display:flex;align-items:center;justify-content:center}

/* about + testimonial */
.feature{top:1238px;height:159px;border-radius:6px;overflow:hidden;background:var(--red);box-shadow:0 2px 4px rgba(0,0,0,.2)}
.feature.about{left:110px;width:477px}
.feature.quote{left:613px;width:475px}
.feature-photo{left:0;top:0;width:210px;height:159px}
.about .feature-photo{background:linear-gradient(90deg,#b04ac0,#d0111b)}
.quote .feature-photo{background:linear-gradient(90deg,#2e4a7a,#d0111b)}
.feature h3{position:absolute;left:218px;top:28px;font-size:18px;color:var(--white);font-weight:400}
.quote h3{left:182px}
.feature p{position:absolute;left:218px;top:58px;width:235px;font-size:11.5px;line-height:23px;color:var(--white);text-align:justify}
.quote p{left:182px;width:270px}
.quote .author{top:112px;font-weight:700}
.read-more{position:absolute;right:0;bottom:0}
.arrows{position:absolute;right:18px;bottom:18px;display:flex;gap:6px}

/* newsletter */
.newsletter{left:0;top:1440px;width:1200px;height:201px;background:var(--charcoal)}
.newsletter .section-title{top:30px;color:var(--white);font-size:26px}
.newsletter-sub{left:0;top:72px;width:1200px;text-align:center;color:#ddd;font-size:15px}
.field{top:106px;height:49px;border:1px solid #aaa;border-radius:25px;color:#ddd;font-size:11px;padding:17px 18px}
.field.name{left:221px;width:266px}
.field.email{left:505px;width:277px}
.submit{left:797px;top:106px;width:179px;height:49px;border-radius:25px;background:linear-gradient(#e0141f,#a80a12);color:var(--white);font-weight:700;font-size:16px;display:flex;align-items:center;justify-content:center}

/* blog */
.blog{left:0;top:1641px;width:1200px;height:271px;background:var(--paper-light)}
.blog .section-title{top:32px;font-size:26px}
.post-thumb{top:97px;width:195px;height:128px;border:4px solid var(--white);box-shadow:0 3px 6px rgba(0,0,0,.25)}
.post-thumb.one{left:115px;background:linear-gradient(135deg,#5d5a52,#a89a84)}
.post-thumb.two{left:614px;background:linear-gradient(135deg,#2a3a5a,#7a8a9a)}
.post{top:94px;width:260px}
.post.one{left:330px}.post.two{left:831px}
.post h4{font-weight:400;font-size:13px;line-height:22px;color:#444}
.post .meta{font-size:10px;color:#666;margin:10px 0 8px}
.post .meta b{color:var(--red);font-weight:400}
.post p{font-size:11px;line-height:24px;color:#999}

/* partners */
.partners{left:0;top:1912px;width:1200px;height:120px;background:var(--grey-band);display:flex;align-items:center;justify-content:space-between;padding:0 112px}
.partners span{width:100px;height:34px;background:#b8b8b8;border-radius:4px;display:block}

/* footer */
.site-footer{left:0;top:2032px;width:1200px;height:163px;background:var(--paper)}
.site-footer .brand{left:110px;top:53px}
.divider{top:22px;width:1px;height:118px;background:#ccc}
.foot-links{top:45px;font-size:11px;color:#555;line-height:34px}
.foot-links li{list-style:none;display:flex;align-items:center;gap:5px}
.foot-links li::before{content:"";width:9px;height:9px;border-radius:50%;border:2px solid var(--red)}
.site-footer .social{left:871px;top:63px}
.site-footer .social span{width:42px;height:42px}
.copyright{left:0;top:2195px;width:1200px;height:75px;background:var(--charcoal);color:#ddd;font-size:11px;text-align:center;line-height:70px}
</style>
</head>
<body>

<header class="site-header abs">
  <div class="brand abs"><span class="brand-mark"></span><span class="brand-name">Apexa Growth Partners</span></div>
  <div class="social abs"><span></span><span></span><span></span><span></span></div>
  <nav class="main-nav abs">
    <a class="active">HOME</a><a>SERVICES</a><a>IMPACT STORIES</a><a>MEDIA</a><a>ABOUT</a><a>RESOURCES</a><a>CONTACT</a>
  </nav>
</header>
<div class="call-tab abs">
  <svg width="20" height="20" viewBox="0 0 20 20"><circle cx="10" cy="10" r="9" fill="none" stroke="#fff" stroke-width="1.5"/><path d="M7 5l2 2-1 1.5a6 6 0 0 0 3.5 3.5L13 11l2 2-1.5 1.5C10 14 6 10 5.5 6.5z" fill="#fff"/></svg>
  Call Us +1 555 010 4400
</div>

<section class="hero abs" role="img" aria-label="Photo of the coach speaking into a microphone on stage"></section>
<h1 class="hero-title abs">APEXA GROWTH PARTNERS</h1>
<div class="hero-rule abs"></div>
<p class="hero-lead abs">Lorem ipsum dolor sit amet, consectetur adipiscing elit. Proin pharetra ante sed semper elementum. Praesent in neque id risus iaculis rhoncus vel ut dolor. Pellentesque scelerisque tempus felis.</p>
<div class="dots abs"><i></i><i></i><i class="on"></i><i></i></div>

<section class="services abs"></section>
<div class="card coach abs" role="img" aria-label="Photo of the coach presenting on a lit stage"></div>
<div class="card speaker abs" role="img" aria-label="Photo of the coach speaking at an event"></div>
<div class="card programs abs" role="img" aria-label="Portrait photo of the coach in a studio"></div>
<p class="card-note abs">Lorem ipsum dolor sit amet, consectetur adipiscing elit. Proin pharetra ante sed semper elementum. Praesent in neque id risus iaculis rhoncus vel ut dolor.</p>
<div class="pill abs" style="left:134px">BUSINESS COACH</div>
<div class="pill red abs" style="left:469px">PUBLIC SPEAKER</div>
<div class="pill abs" style="left:803px">SUCCESS PROGRAMS</div>

<section class="expertise abs">
  <h2 class="section-title abs">EXPERT IN BUSINESS COACH</h2>
  <p class="expertise-copy abs">Donec at mauris varius, iaculis neque sed, pharetra quam. Morbi eget lorem nec purus pellentesque egestas eu a nibh. Phasellus non erat hendrerit, consectetur metus eu, laoreet dolor. Nulla ornare pharetra tempus. Cras luctus nibh nec felis volutpat, non aliquet nisi porta. Mauris pulvinar massa convallis, commodo sapien sit amet, commodo quam. Proin tincidunt et velit at pellentesque. Suspendisse dapibus et quam sed commodo. Sed et sem sem. Etiam ante nunc, fermentum a blandit vel, imperdiet nec nulla.</p>
  <div class="events-btn abs">UPCOMING EVENTS</div>
</section>

<article class="feature about abs">
  <div class="feature-photo abs" role="img" aria-label="Photo of the coach gesturing on stage"></div>
  <h3>ABOUT ME</h3>
  <p>Aliquam pulvinar enim lacus, sit amet consectetur felis faucibus vel. Nullam mauris eros, commodo.</p>
  <svg class="read-more" width="60" height="60" viewBox="0 0 60 60"><path d="M60 0V60H0z" fill="#1a1a1a"/><text x="40" y="46" fill="#fff" font-family="Open Sans,sans-serif" font-size="9" font-weight="700" transform="rotate(-45 40 46)" text-anchor="middle">READ</text><text x="47" y="53" fill="#fff" font-family="Open Sans,sans-serif" font-size="9" font-weight="700" transform="rotate(-45 47 53)" text-anchor="middle">MORE</text></svg>
</article>
<article class="feature quote abs">
  <div class="feature-photo abs" role="img" aria-label="Photo of the coach seated in a television studio"></div>
  <h3>WHAT PEOPLE SAY ABOUT ME</h3>
  <p>Suspendisse dapibus et quam sed commodo. Sed et sem sem. Etiam ante nunc, fermentum...</p>
  <p class="author">- LENA MARSH</p>
  <div class="arrows">
    <svg width="15" height="15" viewBox="0 0 15 15"><circle cx="7.5" cy="7.5" r="7.5" fill="#fff"/><path d="M9 4L5.5 7.5 9 11" fill="none" stroke="#d0111b" stroke-width="2"/></svg>
    <svg width="15" height="15" viewBox="0 0 15 15"><circle cx="7.5" cy="7.5" r="7.5" fill="#fff"/><path d="M6 4l3.5 3.5L6 11" fill="none" stroke="#d0111b" stroke-width="2"/></svg>
  </div>
</article>

<section class="newsletter abs">
  <h2 class="section-title abs">SIGN-UP OUR NEWSLETTER</h2>
  <p class="newsletter-sub abs">Join our mailing list.</p>
  <div class="field name abs">Name</div>
  <div class="field email abs">Email Address</div>
  <div class="submit abs">SUBMIT</div>
</section>

<section class="blog abs">
  <h2 class="section-title abs">LATEST BLOG</h2>
  <div class="post-thumb one abs" role="img" aria-label="Photo of an audience seated in rows"></div>
  <div class="post one abs">
    <h4>Ut wisi enim ad minim veniam, quis nostr ud exerci tation ullamcorper</h4>
    <div class="meta"><b>&#9632;</b> 27 Dec 2015 &nbsp; <b>&#9650;</b> Share</div>
    <p>Duis autem vel eum iriure dolor in hendrerit in vulputate velit esse molestie consequat...</p>
  </div>
  <div class="post-thumb two abs" role="img" aria-label="Photo of a studio interview"></div>
  <div class="post two abs">
    <h4>Vivamus vitae ultrices quam, eget faucibus tortor. Integer arcu sem,</h4>
    <div class="meta"><b>&#9632;</b> 27 Dec 2015 &nbsp; <b>&#9650;</b> Share</div>
    <p>Duis autem vel eum iriure dolor in hendrerit in vulputate velit esse molestie consequat...</p>
  </div>
</section>

<section class="partners abs">
  <span></span><span></span><span></span><span></span><span></span><span></span><span></span><span></span>
</section>

<footer class="site-footer abs">
  <div class="brand abs"><span class="brand-mark"></span><span class="brand-name">Apexa Growth Partners</span></div>
  <div class="divider abs" style="left:295px"></div>
  <ul class="foot-links abs" style="left:339px"><li>HOME</li><li>SERVICES</li><li>IMPACT STORIES</li></ul>
  <ul class="foot-links abs" style="left:520px"><li>MEDIA</li><li>ABOUT</li><li>BLOG</li></ul>
  <ul class="foot-links abs" style="left:664px"><li>EVENTS</li><li>PRIVACY POLICY</li><li>SITEMAP</li></ul>
  <div class="divider abs" style="left:834px"></div>
  <div class="social abs"><span></span><span></span><span></span><span></span></div>
</footer>
<div class="copyright abs">Copyrights@2016 Apexa Growth Partners. All Rights Reserved.</div>

</body>
</html>
```